Marine Electronics Manufacturer needs an infographic for aquaculture related product

Dissolved CO2 Removal For Fish Transport Infographic

Background
When fish breathe underwater they pass water over their gills and absorb dissolved oxygen (O2) from the water and at the same time release CO2 into the water as dissolved gas. The process is similar to humans, with the exception that the O2 and CO2 is absorbed from the water rather than being breathed in as a gas. When live fish are transported by road, rail or air they are typically packed into large sealed bins with water and one of the challenges is to be able to fit enough fish onto a bin to make it commercially viable, while maintaining the health and welfare of the fish. And the more fish you have the more CO2 will be released into the water, which often contributes to high mortality rates and poor health outcomes for the fish. So the removal of the CO2 from the water during transport is often essential to being able to achieve the dual outcomes of market viability and healthy fish.

Infographic Requirements
The infographic needs to illustrate clearly the process described below for the removal of dissolved CO2 from the water in sealed live fish transport bins. Also see the attached image that provides a graphical description of the key processes.

- Live fish are transported in sealed bins with water
- Fish take in O2 from the water and at the same time expel CO2 into the water as part of respiration.
- Keeping CO2 levels in the in the water low improves the survival of the fish results in better health outcomes.
- The process selectively removes CO2 from the water using a gas specific membrane that water is pumped through
- There is a sweep gas (air) from outside the bin is pumped through the membrane in the reverse direction to the water that takes the CO2 removed from the water and expels it outside the bin.
- The water is continuously re-circulating through the system and the air is always fresh from outside the system with no re-circulation.

Please include:

- Option for Harbor Crest logo to be included
- Harbor crest URL harborcrest-example.com.au
- Please use logo colours for guidance on the colour scheme of overall graphic.

```html
<!DOCTYPE html>
<html lang="en">
<head>
<meta charset="utf-8">
<title>Dissolved CO2 Removal for Fish Transport</title>
<link rel="stylesheet" href="https://fonts.googleapis.com/css2?family=Bebas+Neue&family=Poppins:wght@500;600;700&display=swap">
<style>
:root{
  --stage:#e4e4e4;
  --sea-top:#2a9cf4;
  --sea-mid:#17c0f9;
  --sea-low:#2aa6f7;
  --ink-white:#ffffff;
  --title-blue:#1d5fe6;
  --fish-yellow:#e9c43a;
  --fish-dark:#2b2b2b;
  --clown-orange:#f07a1a;
}
*{margin:0;padding:0;box-sizing:border-box}
html,body{width:1009px;height:1200px;overflow:hidden;background:var(--stage)}
.poster{
  position:absolute;left:81px;top:0;width:847px;height:1200px;overflow:hidden;
  background:linear-gradient(180deg,var(--sea-top) 0%,var(--sea-mid) 45%,var(--sea-low) 100%);
  font-family:"Poppins",sans-serif;color:var(--ink-white);
}
.brand{
  position:absolute;top:30px;left:0;width:100%;display:flex;justify-content:center;align-items:center;gap:10px;
}
.brand-mark{width:42px;height:42px;background:var(--ink-white);border-radius:4px}
.brand-name{font-weight:700;font-size:42px;letter-spacing:-1.5px;line-height:1}
.title-box{
  position:absolute;left:115px;top:97px;width:621px;height:89px;background:var(--ink-white);border-radius:14px;
  display:flex;align-items:center;justify-content:center;overflow:hidden;
}
.title{
  font-family:"Bebas Neue",sans-serif;font-size:60px;font-weight:400;color:var(--title-blue);letter-spacing:-0.5px;
  transform:skewX(-12deg) scaleX(.72);transform-origin:center;white-space:nowrap;line-height:1;
}
.bubble{
  position:absolute;width:158px;height:158px;margin:-79px 0 0 -79px;border-radius:50%;
  background:radial-gradient(circle at 35% 30%,rgba(255,255,255,.35),rgba(255,255,255,.1) 55%,rgba(255,255,255,.22) 100%);
  border:2px solid rgba(255,255,255,.55);box-shadow:0 8px 14px rgba(0,60,140,.25);
  display:flex;align-items:center;justify-content:center;
}
.bubble svg{width:104px;height:104px;fill:none;stroke:var(--ink-white);stroke-width:3.5;stroke-linecap:round;stroke-linejoin:round}
.bubble text{fill:var(--ink-white);stroke:none;font-family:"Poppins",sans-serif;font-weight:500}
.step{
  position:absolute;font-weight:500;font-size:22.5px;line-height:26px;letter-spacing:-.9px;transform:translateY(-50%);
}
.step.left{left:253px}
.step.right{text-align:right}
.fish-art{position:absolute}
.fish-school{left:27px;top:21px;width:139px;height:110px;border-radius:40%;background:radial-gradient(circle,rgba(240,230,160,.6),rgba(40,40,40,.25) 60%,transparent 75%)}
.fish-yellow{left:783px;top:537px;width:64px;height:94px;border-radius:50% 0 0 50%;background:linear-gradient(135deg,var(--fish-yellow),var(--fish-dark))}
.fish-clown{left:0;top:1069px;width:155px;height:131px;border-radius:0 60% 0 0;background:linear-gradient(135deg,var(--clown-orange),#c85a10)}
</style>
</head>
<body>
<main class="poster">
  <div class="fish-art fish-school" role="img" aria-label="Illustration of a small school of striped reef fish"></div>
  <div class="fish-art fish-yellow" role="img" aria-label="Illustration of a yellow and black reef fish"></div>
  <div class="fish-art fish-clown" role="img" aria-label="Illustration of an orange clownfish"></div>

  <header class="brand">
    <span class="brand-mark"></span>
    <span class="brand-name">harborcrest</span>
  </header>
  <div class="title-box"><h1 class="title">DISSOLVED CO2 REMOVAL FOR FISH TRANSPORT</h1></div>

  <!-- Step 1: sealed bin -->
  <div class="bubble" style="left:150px;top:288px">
    <svg viewBox="0 0 100 100"><rect x="14" y="22" width="72" height="12"/><path d="M20 34v40h60V34M22 22v-8h10v8M36 22v-8h10v8M50 22v-8h10v8M64 22v-8h10v8M24 74v6M76 74v6M28 40h44"/></svg>
  </div>
  <p class="step left" style="top:282px">Live fish are transported in sealed bins<br>with water</p>

  <!-- Step 2: respiration -->
  <div class="bubble" style="left:677px;top:418px">
    <svg viewBox="0 0 100 100"><text x="22" y="48" font-size="20">CO₂</text><path d="M50 30c12 0 20 8 20 8M66 32l4 6-7 1"/><text x="48" y="72" font-size="20">O₂</text><path d="M42 66c-10 0-16-6-16-6M30 66l-4-6 7-1"/></svg>
  </div>
  <p class="step right" style="top:428px;right:281px">Fish take in O2 from the water &amp; at<br>the same time expel CO2 into the<br>water as part of respiration</p>

  <!-- Step 3: gauge -->
  <div class="bubble" style="left:150px;top:557px">
    <svg viewBox="0 0 100 100"><path d="M14 60a36 36 0 0 1 72 0"/><path d="M50 24v6M24 35l4 4M76 35l-4 4"/><circle cx="70" cy="59" r="3" fill="#fff"/><path d="M36 55l34 4"/><text x="10" y="82" font-size="12" stroke="none">LOW</text><text x="66" y="82" font-size="12" stroke="none">HIGH</text></svg>
  </div>
  <p class="step left" style="top:566px">Keeping CO2 levels in the water low<br>improves the survival of the fish results<br>in better health outcomes.</p>

  <!-- Step 4: membrane -->
  <div class="bubble" style="left:677px;top:698px">
    <svg viewBox="0 0 100 100"><path d="M18 44h64M18 52h64M18 60h64M18 68h64M30 40V20M50 40V16M70 40V20M24 26l6-6 6 6M44 22l6-6 6 6M64 26l6-6 6 6M30 72v14M50 72v14M70 72v14"/></svg>
  </div>
  <p class="step right" style="top:725px;right:272px">The process selectively removes CO2<br>from the water using a gas specific<br>membrane that water is pumped<br>through</p>

  <!-- Step 5: sweep air filter -->
  <div class="bubble" style="left:150px;top:882px">
    <svg viewBox="0 0 100 100"><circle cx="20" cy="26" r="5"/><circle cx="34" cy="24" r="4"/><circle cx="46" cy="28" r="3"/><circle cx="60" cy="24" r="5"/><circle cx="76" cy="26" r="4"/><path d="M16 38h68L58 56v10H42V56z M50 42v12M46 50l4 4 4-4"/><circle cx="24" cy="78" r="8"/><circle cx="50" cy="80" r="8"/><circle cx="76" cy="78" r="8"/><path d="M20 78l3 3 5-5M46 80l3 3 5-5M72 78l3 3 5-5"/></svg>
  </div>
  <p class="step left" style="top:897px">There is a sweep air from outside the bin<br>is pumped through the membrane in the<br>reverse direction to the water that takes the<br>CO2 removed from the water and expels it<br>outside the bin.</p>

  <!-- Step 6: recirculation -->
  <div class="bubble" style="left:677px;top:1064px">
    <svg viewBox="0 0 100 100"><path d="M50 30c-8 12-12 18-12 24a12 12 0 0 0 24 0c0-6-4-12-12-24z"/><path d="M44 56a6 6 0 0 0 6 6"/><path d="M20 46a32 32 0 0 1 52-24M80 54a32 32 0 0 1-52 24M66 18l7 4-3 8M34 82l-7-4 3-8"/></svg>
  </div>
  <p class="step right" style="top:1084px;right:295px">The water is continuously<br>re-circulating through the system<br>and the air is always fresh from<br>outside the system with no<br>re-circulation</p>
</main>
</body>
</html>
```